Honigetikett gesucht
Zielgruppe
Ich bin ein Hobbyimker und brauche ein Etikett für meinen Honig. Zielgruppe = Jeder
Aufgabenstellung
Bitte keine schwarzen Etiketten mehr... gefällt uns leider nicht. Danke!
Das Etikett ist für Honig, 500 Gramm Glas. Man muss den gesetzlichen Vorgaben einhalten. https://www.wabenhofportal.at/de/labor/lebensmittelrecht.html
Blütenhonig aus Österreich
Name
Adresse
500 g
Trocken und vor Licht und Wärme geschützt lagern.
Mindestens haltbar bis:
Sichtfeldregelung
Sachbezeichnung und Nettofüllmenge müssen am Etikett in einem Sichtfeld angebracht werden. Ein Sichtfeld ist eine Oberfläche einer Verpackung, die von einem einzigen Blickpunkt aus gelesen werden kann.
Mindesthaltbarkeitsdatum und Lagerbedingungen sind in einem Sichtfeld anzubringen. Dabei muss die Lagerbedingung über oder unter der Haltbarkeit angeführt werden und darf nicht durch Bild- oder Schrift getrennt sein.
Mindestschriftgröße aller verpflichtenden Angaben (Ausnahme Nettofüllmenge) Mindestschriftgröße:
Die verwendete Schrift muss am kleinen „x“ der verwendeten Schriftart gemessen mindestens 1,2mm Höhe ausmachen
Erreicht die Gesamtoberfläche des Gebindes auf dem Ein Etikett angebracht werden kann max. 80cm2, so muss die Höhe am kleinen „x“ der verwendeten Schriftart gemessen mindestens 0,9mm Höhe ausmachen (beim Honigglas wäre dies erst unter dem 125g Glas)
Die Mindestschriftgröße der Nettofüllmenge bleibt davon unberührt und unterliegt weiterhin der Fertigpackungsverordnung (siehe Nettofüllmenge)

```html
<!DOCTYPE html>
<html lang="de">
<head>
<meta charset="UTF-8">
<title>Blütenhonig – Etikett</title>
<link rel="stylesheet" href="https://fonts.googleapis.com/css2?family=Playfair+Display:wght@400&family=Source+Sans+3:wght@400&display=swap">
<style>
  :root {
    --backdrop: #f5f3ee;
    --label-light: #ffffff;
    --ink-dark: #2e2e2e;
    --ink-soft: #5a5a5a;
    --honey: #f3b61a;
    --honey-deep: #e29a0c;
  }
  html, body {
    margin: 0;
    padding: 0;
    width: 1200px;
    height: 1200px;
    overflow: hidden;
    background: var(--backdrop);
  }
  .canvas {
    width: 1200px;
    height: 1200px;
    display: flex;
    justify-content: center;
    align-items: center;
  }
  .label {
    position: relative;
    width: 820px;
    height: 620px;
    background: var(--label-light);
    color: var(--ink-dark);
    box-shadow: 0 8px 30px rgba(0,0,0,0.08);
    font-family: "Source Sans 3", Arial, sans-serif;
  }
  .label p { margin: 0; }

  .label__details {
    position: absolute;
    left: 56px;
    top: 60px;
    width: 300px;
    font-size: 18px;
    line-height: 1.45;
  }
  .label__weight { margin-bottom: 12px !important; }

  .label__keeping {
    position: absolute;
    right: 56px;
    top: 60px;
    width: 250px;
    font-size: 18px;
    line-height: 1.45;
  }
  .label__date { margin-bottom: 8px !important; }

  .label__dipper {
    position: absolute;
    left: 470px;
    top: 222px;
    width: 294px;
    height: 160px;
    border-radius: 56px 10px 10px 56px;
    background: linear-gradient(160deg, var(--honey) 0%, var(--honey-deep) 100%);
  }

  .label__title {
    position: absolute;
    left: 0;
    right: 0;
    top: 410px;
    margin: 0;
    text-align: center;
    font-family: "Playfair Display", Georgia, serif;
    font-weight: 400;
    font-size: 96px;
    letter-spacing: 1px;
    line-height: 1;
  }
  .label__origin {
    position: absolute;
    left: 0;
    right: 0;
    top: 530px;
    text-align: center;
    font-family: "Playfair Display", Georgia, serif;
    font-size: 26px;
    letter-spacing: 6px;
    color: var(--ink-soft);
  }
</style>
</head>
<body>
<main class="canvas">
  <section class="label">
    <div class="label__details">
      <p class="label__weight">500 g</p>
      <p class="label__producer">Imkerei Kravotello<br>Lindengasse 5a<br>3100 Wabenfeld<br>imker@wabenpost.at</p>
    </div>
    <div class="label__keeping">
      <p>Mindestens haltbar bis:</p>
      <p class="label__date">23.02.2025</p>
      <p class="label__storage">Trocken und vor Licht und Wärme geschützt lagern.</p>
    </div>
    <div class="label__dipper" role="img" aria-label="Illustration eines Honiglöffels mit herabtropfendem Honig"></div>
    <h1 class="label__title">BLÜTENHONIG</h1>
    <p class="label__origin">aus Österreich</p>
  </section>
</main>
</body>
</html>
```